women's junior contemporary apparel company.
We are looking for a business card that represents our urban design aesthetic. We would like to keep it simple and modern/contemporary.
the name of the company is 'v-lumen'.

we've attached a font style but you are not limited solely to use this font. All suggestions are welcomed.

Industry/Entity Type

Business

```html
<!DOCTYPE html>
<html lang="en">
<head>
<meta charset="utf-8">
<title>v-lumen business card</title>
<link href="https://fonts.googleapis.com/css2?family=Courier+Prime&display=swap" rel="stylesheet">
<style>
  :root {
    --page-bg: #ececec;
    --mint: #cfe8c6;
    --ink: #111111;
    --swoosh: #0b0b0b;
    --edge-grey: #3a3a3a;
    --url-grey: #3d3d3d;
    --photo-light: #f4f4f4;
    --photo-mid: #d9dbde;
    --photo-denim: #9fb2c9;
  }
  html, body {
    margin: 0;
    padding: 0;
    width: 1100px;
    height: 1200px;
    overflow: hidden;
    background: var(--page-bg);
  }
  .canvas {
    width: 1100px;
    height: 1200px;
    display: flex;
    flex-direction: column;
    align-items: center;
    justify-content: center;
    gap: 60px;
  }
  .card {
    width: 900px;
    height: 514px;
    display: block;
    box-shadow: 0 6px 18px rgba(0,0,0,0.18);
  }
  .type {
    font-family: "Courier Prime", "Courier New", monospace;
    font-weight: 400;
  }
  .wordmark-front { font-size: 72px; fill: var(--ink); }
  .wordmark-back { font-size: 56px; fill: var(--ink); }
  .site-url { font-size: 18px; fill: var(--url-grey); letter-spacing: 2px; }
  .contact-line { font-size: 23px; fill: var(--ink); letter-spacing: 2px; }
  .contact-icon { fill: var(--ink); }
</style>
</head>
<body>
<main class="canvas">

  <svg class="card card-front" viewBox="0 0 900 514" xmlns="http://www.w3.org/2000/svg">
    <defs>
      <linearGradient id="frontPhotoTone" x1="0" y1="0" x2="1" y2="1">
        <stop offset="0" stop-color="#f4f4f4"/>
        <stop offset="0.5" stop-color="#9fb2c9"/>
        <stop offset="1" stop-color="#d9dbde"/>
      </linearGradient>
    </defs>
    <rect class="mint-field" width="900" height="514" fill="var(--mint)"/>
    <path class="photo-area" role="img" aria-label="Fashion photo: model in black tee and ripped jeans lounging on a white sofa"
          d="M0,0 H900 V220 C760,330 420,400 0,370 Z" fill="url(#frontPhotoTone)"/>
    <path class="swoosh" d="M0,370 C420,400 760,330 900,220 V252 C760,395 430,440 0,386 Z" fill="var(--swoosh)"/>
    <text class="type site-url" x="60" y="48">WWW.NORTHLANEWEAR.COM</text>
    <text class="type wordmark-front" x="860" y="478" text-anchor="end">v-lumen</text>
  </svg>

  <svg class="card card-back" viewBox="0 0 900 514" xmlns="http://www.w3.org/2000/svg">
    <defs>
      <linearGradient id="backPhotoTone" x1="0" y1="0" x2="0" y2="1">
        <stop offset="0" stop-color="#f4f4f4"/>
        <stop offset="0.6" stop-color="#d9dbde"/>
        <stop offset="1" stop-color="#c8c8c8"/>
      </linearGradient>
    </defs>
    <rect class="photo-area" role="img" aria-label="Fashion photo: model seen from behind in a black strappy tank and printed shorts"
          width="900" height="514" fill="url(#backPhotoTone)"/>
    <path class="edge-band" d="M400,0 C500,120 520,330 470,514 H500 C545,330 520,120 412,0 Z" fill="var(--edge-grey)"/>
    <path class="mint-panel" d="M0,0 H400 C500,120 520,330 470,514 H0 Z" fill="var(--mint)"/>

    <text class="type wordmark-back" x="210" y="160" text-anchor="middle">v-lumen</text>

    <g class="contact-list">
      <g class="contact-address">
        <path class="contact-icon" d="M70,368 a7,7 0 1 1 14,0 c0,6 -7,13 -7,13 c0,0 -7,-7 -7,-13 z"/>
        <circle cx="77" cy="368" r="2.5" fill="var(--mint)"/>
        <text class="type contact-line" x="98" y="381">YOUR ADDRESS</text>
      </g>
      <g class="contact-email">
        <rect class="contact-icon" x="68" y="407" width="18" height="13" rx="1"/>
        <path d="M68,408 L77,415 L86,408" stroke="var(--mint)" stroke-width="1.6" fill="none"/>
        <text class="type contact-line" x="98" y="420">YOUR EMAIL.COM</text>
      </g>
      <g class="contact-phone">
        <path class="contact-icon" d="M67,448 q10,-7 20,0 v4 h-5 v-3 h-10 v3 h-5 z"/>
        <rect class="contact-icon" x="70" y="452" width="14" height="9" rx="1.5"/>
        <text class="type contact-line" x="98" y="460">YOUR PHONE NUMBER</text>
      </g>
    </g>
  </svg>

</main>
</body>
</html>
```